Newly established winery needs label for its bottles

The Corvel-Tamarin Winery, is a small family owned winery that has been producing wine for little over 3 years. We are now ready to officially start commercializing our products. To do so we are looking for a label for our wine bottles. We are looking for a creative design that will differentiate our bottles from the more conventional labels. We are looking for one label design with 3 color schemes so that we can have a standard look and feel for all three of our wines, while having some differentiation between them with the different color schemes. In summary we are looking for a label that will standout by its uniqueness, simplicity and its modern touch. The label should also reflect the historical significance of the name of the winery. The attached documents offers more detail about the winery, what we are looking for, as well as some technical specification for the label. This label project is also related to a logo project see brief: http://www.pitchvault.ca/project-progress.aspx?briefId=462193). The logo project is now complete and the winning design source files were added to the documents in this brief. Also, details around the information that will need to appear on the label was added to the document list.
Updates
This label project will be on hold temporarily while the logo project is in progress. If you are interested in participating in the logo project, please follow this link: http://www.pitchvault.ca/project-progress.aspx?briefId=462193 Added Wednesday, December 17, 2014
Reason: Deadline extended to give sufficent time for submission and modification to the designs provided.

```html
<!DOCTYPE html>
<html lang="en">
<head>
<meta charset="utf-8">
<title>Corvel-Tamarin Winery – Label Series 2015</title>
<link rel="stylesheet" href="https://fonts.googleapis.com/css2?family=Great+Vibes&family=Tinos&family=Arimo&display=swap">
<style>
  :root {
    --canvas: #ffffff;
    --label-paper: #f2f4ee;
    --frame: #111111;
    --ink: #1a1a1a;
    --ink-soft: #3a3a3a;
    --oval-rim: #c9a86a;
    --sky: #6fb6d8;
    --field-light: #8cc43c;
    --field-dark: #2f6b1e;
    --earth: #b98a55;
    --red-wine: #7b2b2e;
    --rose-wine: #dcab9a;
    --white-wine: #c9a874;
  }
  * { margin: 0; padding: 0; box-sizing: border-box; }
  html, body {
    width: 1200px; height: 1000px; overflow: hidden;
    background: var(--canvas);
  }
  .label-sheet {
    position: absolute;
    left: 10px; top: 266px;
    width: 1182px; height: 488px;
    display: flex;
    border: 3px solid var(--frame);
  }
  .label {
    position: relative;
    background: var(--label-paper);
    text-align: center;
    color: var(--ink);
  }
  .label + .label { border-left: 3px solid var(--frame); }
  .label--red { width: 386px; }
  .label--rose { width: 385px; }
  .label--white { width: 405px; }

  .winery-name {
    position: absolute; left: 0; right: 0;
    font-family: "Great Vibes", cursive;
    font-size: 31px; line-height: 1;
    color: var(--ink-soft);
  }
  .winery-name--en { top: 50px; }
  .winery-name--fr { top: 234px; }

  .vineyard-scene {
    position: absolute;
    left: 50%; top: 88px;
    width: 108px; height: 140px;
    margin-left: -54px;
    border-radius: 50%;
    border: 2px solid var(--oval-rim);
    background:
      linear-gradient(180deg, var(--sky) 0%, var(--sky) 10%, var(--earth) 14%, var(--earth) 24%, var(--field-light) 34%, var(--field-dark) 100%);
  }

  .origin {
    position: absolute; left: 0; right: 0; top: 263px;
    font-family: "Arimo", sans-serif;
    font-size: 8px; color: var(--ink-soft);
  }
  .vintage {
    position: absolute; left: 0; right: 0; top: 300px;
    font-family: "Tinos", serif;
    font-size: 38px; line-height: 1;
  }
  .wine-type {
    position: absolute; left: 0; right: 0; top: 350px;
    font-family: "Great Vibes", cursive;
    font-size: 38px; line-height: 1;
    text-shadow: 1px 2px 2px rgba(0,0,0,0.25);
  }
  .label--red .wine-type { color: var(--red-wine); }
  .label--rose .wine-type { color: var(--rose-wine); }
  .label--white .wine-type { color: var(--white-wine); }

  .bottle-facts {
    position: absolute; left: 0; right: 0; top: 465px;
    font-family: "Tinos", serif;
    font-size: 12px; word-spacing: 3px;
  }
</style>
</head>
<body>
  <main class="label-sheet">
    <section class="label label--red">
      <p class="winery-name winery-name--en">Winery Corvel-Tamarin</p>
      <div class="vineyard-scene" role="img" aria-label="Painted vineyard rows on rolling hills under a blue sky"></div>
      <p class="winery-name winery-name--fr">Vignoble Corvel-Tamarin</p>
      <p class="origin">Product of Quebec / Produit du Québec</p>
      <p class="vintage">2015</p>
      <p class="wine-type">Red Wine | Vin Rouge</p>
      <p class="bottle-facts">750 ml &nbsp;11.6% alc./Vol.</p>
    </section>
    <section class="label label--rose">
      <p class="winery-name winery-name--en">Winery Corvel-Tamarin</p>
      <div class="vineyard-scene" role="img" aria-label="Painted vineyard rows on rolling hills under a blue sky"></div>
      <p class="winery-name winery-name--fr">Vignoble Corvel-Tamarin</p>
      <p class="origin">Product of Quebec / Produit du Québec</p>
      <p class="vintage">2015</p>
      <p class="wine-type">Rosé | Rosé</p>
      <p class="bottle-facts">750 ml &nbsp;11.6% alc./Vol.</p>
    </section>
    <section class="label label--white">
      <p class="winery-name winery-name--en">Winery Corvel-Tamarin</p>
      <div class="vineyard-scene" role="img" aria-label="Painted vineyard rows on rolling hills under a blue sky"></div>
      <p class="winery-name winery-name--fr">Vignoble Corvel-Tamarin</p>
      <p class="origin">Product of Quebec / Produit du Québec</p>
      <p class="vintage">2015</p>
      <p class="wine-type">White Wine | Vin Blanc</p>
      <p class="bottle-facts">750 ml &nbsp;11.6% alc./Vol.</p>
    </section>
  </main>
</body>
</html>
```